Upscale Wine Cooler/Ready to drink Can Design

We need to design the branding and packaging for a new wine cooler that will be sold in a can. We are also looking for the brand name at this point, so you can be as creative as you can!

The product will have 3 flavours (Cavoni Spritz, Ginger-Lime Spritz, Raspeberry-Mimosa) and will be made of genuine high quality European Wine, with natural flavours

Can dimensions : Height 157 mm ; Diameter : 58 mm
Updates

Need extra days to review

Target Market(s)

Females 19 to 35, who are looking for an alternative to the traditional alcoholic beverages, and who want to drink an upscale and "classy" beverage

Colors

Designer to choose colors to be used in the design.

Requirements
Must have
• Modern, attractive and upscale look
• Brand name
• 3 different cans for each of the flavours : Cavoni Spritz, Ginger-Lime Spritz, Raspeberry-Mimosa
• 355 ml
• 5% alc./vol.

```html
<!DOCTYPE html>
<html lang="en">
<head>
<meta charset="utf-8">
<title>Velvara – Can Labels</title>
<link rel="stylesheet" href="https://fonts.googleapis.com/css2?family=Italianno&family=Didact+Gothic&display=swap">
<style>
  :root {
    --night: #020918;
    --gold: #d7c576;
    --gold-light: #eee08e;
    --gold-deep: #8f7b2c;
    --black: #030303;
    --bottle-green: #031407;
    --disc: #3b3a30;
    --white: #ffffff;
    --edge: #e7ddd0;
  }
  * { margin: 0; padding: 0; box-sizing: border-box; }
  html, body { width: 1034px; height: 1200px; overflow: hidden; background: var(--night); }
  .board { position: relative; width: 1034px; height: 1200px; }
  .label { position: absolute; top: 24px; width: 302px; height: 810px; border: 1px solid var(--edge); }
  .label svg, .mini svg { display: block; width: 100%; height: 100%; }
  .label--cavoni { left: 24px; }
  .label--ginger { left: 368px; }
  .label--raspberry { left: 694px; }
  .presentation { position: absolute; top: 857px; height: 343px; background: var(--white); }
  .presentation--can { left: 26px; width: 325px; }
  .presentation--bottle { left: 370px; width: 340px; }
  .mini { position: absolute; width: 90px; height: 241px; top: 50px; left: 50%; transform: translateX(-50%); }
  .bg-gold { fill: var(--gold); }
  .panel { fill: var(--black); }
  .panel-shade { fill: var(--bottle-green); }
  .glass { fill: url(#glassTone); }
  .star { fill: var(--gold); stroke: var(--gold-deep); stroke-width: 1.5; }
  .arc-rule { fill: none; stroke: var(--gold-deep); stroke-width: 3; }
  .disc { fill: var(--disc); opacity: .8; }
  .rule { stroke: var(--gold); stroke-width: 7; }
  .brand { font-family: "Didact Gothic", sans-serif; font-size: 66px; fill: var(--gold-light); text-anchor: middle; letter-spacing: 2px; }
  .flavour { font-family: "Didact Gothic", sans-serif; font-size: 22px; fill: var(--gold); text-anchor: middle; letter-spacing: 1px; }
  .tagline { font-family: "Italianno", cursive; font-size: 44px; fill: var(--gold); text-anchor: middle; }
  .spec { font-family: "Didact Gothic", sans-serif; font-size: 27px; fill: var(--black); text-anchor: middle; font-weight: 700; }
</style>
</head>
<body>
<main class="board">
  <svg width="0" height="0" style="position:absolute" aria-hidden="true">
    <defs>
      <linearGradient id="glassTone" x1="0" y1="0" x2="1" y2="0">
        <stop offset="0" stop-color="#1c1a10"/>
        <stop offset=".35" stop-color="#8a7a3a"/>
        <stop offset=".6" stop-color="#cdbb6a"/>
        <stop offset="1" stop-color="#1a1a12" stop-opacity=".2"/>
      </linearGradient>
      <g id="labelBase">
        <rect class="bg-gold" width="378" height="1013"/>
        <path class="panel" d="M0,250 C40,125 190,55 378,48 L378,700 C330,860 190,935 0,965 Z"/>
        <rect class="panel-shade" x="270" y="60" width="108" height="720" opacity=".8"/>
        <path class="arc-rule" d="M0,232 C45,110 190,40 378,34"/>
        <rect class="glass" x="8" y="110" width="140" height="850" rx="20" opacity=".55"/>
        <polygon class="star" points="25,95 29,107 42,107 32,115 36,128 25,120 14,128 18,115 8,107 21,107"/>
        <polygon class="star" transform="translate(30,-27)" points="25,95 29,107 42,107 32,115 36,128 25,120 14,128 18,115 8,107 21,107"/>
        <polygon class="star" transform="translate(62,-50)" points="25,95 29,107 42,107 32,115 36,128 25,120 14,128 18,115 8,107 21,107"/>
        <polygon class="star" transform="translate(96,-67)" points="25,95 29,107 42,107 32,115 36,128 25,120 14,128 18,115 8,107 21,107"/>
        <polygon class="star" transform="translate(132,-80)" points="25,95 29,107 42,107 32,115 36,128 25,120 14,128 18,115 8,107 21,107"/>
        <circle class="disc" cx="205" cy="495" r="160"/>
        <line class="rule" x1="0" y1="452" x2="48" y2="452"/>
        <line class="rule" x1="335" y1="452" x2="378" y2="452"/>
        <line class="rule" x1="0" y1="525" x2="48" y2="525"/>
        <line class="rule" x1="335" y1="525" x2="378" y2="525"/>
        <text class="brand" x="205" y="505">Velvara</text>
        <text class="tagline" x="190" y="690">High quality</text>
        <text class="tagline" x="190" y="728">A natural feeling</text>
        <text class="tagline" x="190" y="766">and</text>
        <text class="tagline" x="190" y="804">"Classy"</text>
        <text class="spec" x="208" y="965">355 ml</text>
        <text class="spec" x="200" y="993">5% alc./vol.</text>
      </g>
    </defs>
  </svg>

  <section class="label label--cavoni">
    <svg viewBox="0 0 378 1013" role="img" aria-label="Cavoni Spritz label with a sparkling wine flute photo on the left">
      <use href="#labelBase"/>
      <text class="flavour" x="205" y="560">Cavoni Spritz</text>
    </svg>
  </section>

  <section class="label label--ginger">
    <svg viewBox="0 0 378 1013" role="img" aria-label="Ginger-Lime Spritz label with a sparkling wine flute photo on the left">
      <use href="#labelBase"/>
      <text class="flavour" x="205" y="560">Ginger-Lime Spritz</text>
    </svg>
  </section>

  <section class="label label--raspberry">
    <svg viewBox="0 0 378 1013" role="img" aria-label="Raspeberry-Mimosa label with a sparkling wine flute photo on the left">
      <use href="#labelBase"/>
      <text class="flavour" x="205" y="560">Raspeberry-Mimosa</text>
    </svg>
  </section>

  <section class="presentation presentation--can">
    <div class="mini">
      <svg viewBox="0 0 378 1013" role="img" aria-label="Raspeberry-Mimosa label as applied to the can">
        <use href="#labelBase"/>
        <text class="flavour" x="205" y="560">Raspeberry-Mimosa</text>
      </svg>
    </div>
  </section>

  <section class="presentation presentation--bottle">
    <div class="mini">
      <svg viewBox="0 0 378 1013" role="img" aria-label="Raspeberry-Mimosa label as applied to the bottle">
        <use href="#labelBase"/>
        <text class="flavour" x="205" y="560">Raspeberry-Mimosa</text>
      </svg>
    </div>
  </section>
</main>
</body>
</html>
```